International Dental Education Website

This project is for a small teaching center on endodontic and micro dentistry in Norway. We need a Wordpress website design to display and highlight dental educational courses. Please use our new logo - see attached file. We like lighter, pastel oriented colors. The following sites are nicely laid out and you can use these as a guideline of sorts but I do want a unique site.
http://vorelta.nl/en, http://www.trasmolin.com/Education.aspx?currentSection=courses&cid=14,
http://www.kapiverno.com/.
Please create a space for a possible video on the home page. Please include a small contact form on the home page(name, email, phone, text box). Would like a horizonatal naviagtion bar. Would like an image to go across the whole top part of the site and this may rotate. Please use a stock image that shows a classroom type setting. Put phone number at the top of the screen. Put address and sitemap in a footer.

Reason: Upcoming vacation with limited internet access. Please continue to submit any designs. Thanks you.

Reason: The client is from a foreign country and is on an extended vacation.

Target Market(s)

General dentists (GPs) and specialists in Endodontics

Industry/Entity Type

Dental

Requirements
Must have
• Sitemap: HOME, COURSES, LECTURER, CONTACT US,
NORWEGIAN/ENGLISH. Phone number is: +47 93516072. Business name and address: Vatu Lok AS, Endodontic Teaching Center,
Solbergs vei 14C, 0291 Oslo, Norway.

```html
<!DOCTYPE html>
<html lang="en">
<head>
<meta charset="utf-8">
<title>Vatu Lok – Endodontic Teaching Center</title>
<link rel="stylesheet" href="https://fonts.googleapis.com/css2?family=PT+Sans:wght@400;700&family=PT+Sans+Narrow&family=Gelasio:ital@0;1&display=swap">
<style>
:root{
  --ink:#222;
  --grey-band:#9b9b9b;
  --grey-box:#cbcbcb;
  --grey-line:#8e8e8e;
  --mint:#ccffff;
  --mint-pale:#e9fdfd;
  --mint-text:#cffcfc;
  --teal:#7fd0d3;
  --dark:#3f3f3f;
  --white:#fff;
}
*{margin:0;padding:0;box-sizing:border-box}
html,body{width:1200px;height:900px;overflow:hidden}
body{position:relative;background:var(--white);font-family:"PT Sans",sans-serif;color:var(--ink)}
.abs{position:absolute}

/* header */
.top-rule{left:0;top:0;width:1200px;height:8px;background:#a8a8a8}
.logo{left:208px;top:36px;font-size:30px;font-weight:700;color:var(--teal);letter-spacing:-.5px;line-height:36px}
.phone-panel{left:411px;top:6px;width:658px;height:62px;background:var(--grey-band);border:2px solid #d4d4d4;border-top:none;border-radius:0 0 14px 14px}
.phone-icon{left:467px;top:5px}
.phone-number{left:529px;top:12px;font-size:29px;color:var(--mint-text);letter-spacing:.5px}
.lang{top:17px;height:26px;width:136px;background:var(--dark);border-radius:8px;color:var(--mint-text);font-size:18px;line-height:26px;padding-left:29px}
.lang::before{content:"";position:absolute;left:10px;top:8px;width:10px;height:10px;border-radius:50%;background:var(--teal);box-shadow:0 0 0 2px #2a2a2a}
.lang-no{left:754px}
.lang-en{left:896px}

.search-icon{left:694px;top:77px;width:38px;height:30px;background:#9d9d9d}
.search-field{left:733px;top:77px;width:236px;height:30px;background:#e6e6e6;font-family:"Gelasio",serif;font-style:italic;font-size:19px;color:#8a8a8a;padding:2px 10px}
.search-btn{left:974px;top:76px;width:88px;height:32px;background:linear-gradient(#6a6a6a,#2e2e2e);border:1px solid #111;color:var(--white);font-family:"Gelasio",serif;font-style:italic;font-size:18px;padding:1px 10px}

/* body band */
.page-bg{left:0;top:173px;width:1200px;height:600px;background:var(--mint)}
.content-panel{left:136px;top:173px;width:935px;height:590px;background:var(--mint-pale)}

.nav{left:136px;top:122px;width:935px;height:52px;border-radius:10px 10px 0 0;background:linear-gradient(#a8a8a8 0%,#c9f1f1 30%,#bffcfc 100%)}
.nav-item{top:141px;font-size:18.5px;letter-spacing:1px;color:#2d2d2d}
.nav-item.active{text-decoration:underline;text-underline-offset:3px}
.nav-sep{top:138px;width:2px;height:25px;background:#8d9b9b;box-shadow:1px 0 0 #eef}

/* slider */
.slide-photo{left:143px;top:179px;width:920px;height:355px;background:linear-gradient(120deg,#5a3a2c 0%,#7b5a48 35%,#a58a76 60%,#5e4438 100%)}
.slide-shade{left:143px;top:179px;width:300px;height:355px;background:rgba(25,18,14,.55)}
.slide-arrows{left:170px;top:208px}
.slide-caption{left:164px;top:273px;width:253px;height:203px;background:rgba(150,190,190,.75);padding:4px 8px;color:var(--white);font-family:"Gelasio",serif}
.slide-caption h2{font-weight:400;font-size:34px;line-height:42px;margin-bottom:20px}
.slide-caption p{font-size:15.5px;line-height:22.5px}
.slide-more{left:338px;top:496px;font-family:"Gelasio",serif;font-size:16px;color:var(--white)}

/* boxes */
.section-title{top:541px;font-size:20px;letter-spacing:.5px;color:#333;text-shadow:2px 3px 3px rgba(0,0,0,.25)}
.box{background:var(--grey-box);border:1px solid var(--grey-line);border-radius:3px}
.contact-box{left:143px;top:566px;width:520px;height:179px}
.field-label{font-family:Arial,sans-serif;font-size:13px;color:#222}
.field{background:var(--white);border-radius:3px}
.pill{background:var(--mint);border-radius:11px;font-size:10px;text-align:center;color:#222}

.video-box{left:669px;top:566px;width:396px;height:179px}
.video-frame{left:674px;top:570px;width:205px;height:171px;background:linear-gradient(#d9d4cc 0%,#c9c2b8 50%,#6b645e 100%)}
.video-bar{left:674px;top:726px;width:205px;height:15px;background:#111}
.video-text{left:884px;top:586px;width:171px;font-family:"PT Sans Narrow",sans-serif;font-size:13.5px;line-height:19px;text-align:justify;color:#555}

/* footer */
.footer-wave{left:0;top:748px}
.footer-img{left:147px;top:772px;width:142px;height:118px;border-radius:30px 40px 30px 30px;background:radial-gradient(ellipse at 50% 55%,#c8545c 0%,#e7a7a4 45%,#efe3d7 75%,rgba(156,156,156,0) 100%)}
.footer-links{left:157px;top:787px;font-size:14px;line-height:18px;letter-spacing:.5px;color:#111;list-style:none}
.footer-sep{top:777px;width:3px;height:103px;background:var(--mint);box-shadow:2px 2px 3px rgba(0,0,0,.3)}
.footer-map{left:361px;top:784px;width:113px;height:97px;background:linear-gradient(135deg,#e9e5d6,#d2dac4 50%,#eed9a0)}
.footer-heading{font-size:14px;letter-spacing:.5px;color:#111}
.footer-address{left:486px;top:812px;font-size:12.5px;line-height:13.8px;letter-spacing:.8px;color:#111}
.social-note{left:855px;top:810px;font-size:13px;color:#111}
.social{top:851px;width:32px;height:32px;border-radius:5px;box-shadow:1px 2px 2px rgba(0,0,0,.35)}
</style>
</head>
<body>

<header>
  <div class="abs top-rule"></div>
  <div class="abs logo">Vatu Lok</div>

  <div class="abs phone-panel"></div>
  <svg class="abs phone-icon" width="52" height="52" viewBox="0 0 52 52" aria-hidden="true">
    <circle cx="26" cy="26" r="25" fill="#111" stroke="#666" stroke-width="1.5"/>
    <path d="M19 13c2-1 4 0 5 2l2 5c1 2 0 3-1 4l-2 1c1 4 4 7 7 8l1-2c1-1 2-2 4-1l4 3c2 1 2 3 1 5l-2 2c-3 2-9 0-14-5s-8-12-6-16z" fill="#f2f2f2"/>
  </svg>
  <div class="abs phone-number">+47 93516072</div>
  <div class="abs lang lang-no">NORWEGIAN</div>
  <div class="abs lang lang-en">ENGLISH</div>

  <div class="abs search-icon">
    <svg width="38" height="30" viewBox="0 0 38 30" aria-hidden="true">
      <circle cx="15" cy="12" r="6" fill="none" stroke="#fff" stroke-width="3"/>
      <path d="M19 16l8 9" stroke="#fff" stroke-width="4" stroke-linecap="round"/>
    </svg>
  </div>
  <div class="abs search-field">Keyword</div>
  <div class="abs search-btn">Search</div>
</header>

<div class="abs page-bg"></div>
<div class="abs content-panel"></div>

<nav>
  <div class="abs nav"></div>
  <span class="abs nav-item active" style="left:274px">HOME</span>
  <span class="abs nav-sep" style="left:373px"></span>
  <span class="abs nav-item" style="left:421px">COURSES</span>
  <span class="abs nav-sep" style="left:537px"></span>
  <span class="abs nav-item" style="left:590px">LECTURER</span>
  <span class="abs nav-sep" style="left:722px"></span>
  <span class="abs nav-item" style="left:770px">CONTACT US</span>
</nav>

<section class="slider">
  <div class="abs slide-photo" role="img" aria-label="Photo of students seated in a lecture hall taking notes"></div>
  <div class="abs slide-shade"></div>
  <svg class="abs slide-arrows" width="64" height="36" viewBox="0 0 64 36" aria-hidden="true">
    <path d="M18 3L6 18l12 15" fill="none" stroke="#fff" stroke-width="5" stroke-linecap="round" stroke-linejoin="round"/>
    <path d="M46 3l12 15-12 15" fill="none" stroke="#fff" stroke-width="5" stroke-linecap="round" stroke-linejoin="round"/>
  </svg>
  <div class="abs slide-caption">
    <h2>Seminars</h2>
    <p>Etiam mollis sapien et risus laoreet mollis. Maecenas varius mollis lacus, facilisis dapibus nislbibendum sit amet. Quisque molestie adipiscing nulla sit amet Nam ante neque, vehicula nec .</p>
  </div>
  <div class="abs slide-more">Read More</div>
</section>

<section class="contact">
  <h3 class="abs section-title" style="left:159px;font-weight:400">CONTACT US</h3>
  <div class="abs box contact-box"></div>
  <span class="abs field-label" style="left:160px;top:598px">Name</span>
  <div class="abs field" style="left:204px;top:595px;width:170px;height:29px"></div>
  <span class="abs field-label" style="left:162px;top:643px">Email</span>
  <div class="abs field" style="left:204px;top:639px;width:170px;height:29px"></div>
  <span class="abs field-label" style="left:157px;top:688px">Phone</span>
  <div class="abs field" style="left:204px;top:684px;width:170px;height:29px"></div>
  <span class="abs field-label" style="left:390px;top:596px">Message</span>
  <div class="abs field" style="left:386px;top:613px;width:272px;height:93px"></div>
  <div class="abs pill" style="left:600px;top:717px;width:53px;height:20px;line-height:20px">SEND</div>
</section>

<section class="videos">
  <h3 class="abs section-title" style="left:681px;font-weight:400">VIDEOS</h3>
  <div class="abs box video-box"></div>
  <div class="abs video-frame" role="img" aria-label="Video still of a presenter speaking to a seated audience"></div>
  <svg class="abs" style="left:762px;top:633px" width="30" height="32" viewBox="0 0 30 32" aria-hidden="true"><path d="M2 2l26 14L2 30z" fill="#111"/></svg>
  <div class="abs video-bar">
    <svg width="205" height="15" viewBox="0 0 205 15" aria-hidden="true">
      <path d="M4 4l6 3.5L4 11z" fill="#fff"/>
      <text x="18" y="10" font-size="5" fill="#ccc" font-family="Arial">12:10</text>
      <rect x="35" y="6" width="137" height="3" fill="#555"/>
      <rect x="35" y="6" width="105" height="3" fill="#ddd"/>
      <text x="176" y="10" font-size="5" fill="#ccc" font-family="Arial">09:20</text>
      <path d="M193 6h2l3-3v9l-3-3h-2z" fill="#fff"/>
    </svg>
  </div>
  <p class="abs video-text">Lorem Ipsum is simply dummy text of the printing and typesetting industry. Lorem Ipsum has been the industry's standard dummy text ever since the 1500s, when an unknown printer took a galley of type and scrambled .......</p>
  <div class="abs pill" style="left:996px;top:717px;width:53px;height:20px;line-height:8px;padding-top:2px">READ<br>MORE</div>
</section>

<footer>
  <svg class="abs footer-wave" width="1200" height="152" viewBox="0 0 1200 152" aria-hidden="true">
    <path d="M0 10C150 -4 260 22 420 12S700 -2 860 12 1080 20 1200 8V152H0z" fill="#9c9c9c"/>
  </svg>
  <div class="abs footer-img" role="img" aria-label="Illustration of a dental model"></div>
  <ul class="abs footer-links">
    <li>VATU LOK</li><li>HOME</li><li>COURSES</li><li>LECTURER</li><li>CONTACT US</li>
  </ul>
  <div class="abs footer-sep" style="left:304px"></div>
  <div class="abs footer-map" role="img" aria-label="Street map of the center's location in Oslo"></div>
  <div class="abs footer-heading" style="left:487px;top:787px">LOCATION</div>
  <address class="abs footer-address" style="font-style:normal">
    TEL : +47 93516072<br>
    NAME : VATU LOK AS<br>
    ADDRESS :ENDODONTIC TEACHING CENTER,<br>
    SOLBERGS VEI 14C, 0291 OSLO, NORWAY.
  </address>
  <div class="abs footer-sep" style="left:799px"></div>
  <div class="abs footer-heading" style="left:855px;top:787px;letter-spacing:0">SOCIAL NETWORK</div>
  <div class="abs social-note">Find us on these social network sites</div>
  <span class="abs social" style="left:856px;background:#3fa6d8" role="img" aria-label="Social network link"></span>
  <span class="abs social" style="left:897px;background:#3d5c9a" role="img" aria-label="Social network link"></span>
  <span class="abs social" style="left:938px;background:#2f7fb3" role="img" aria-label="Social network link"></span>
  <span class="abs social" style="left:979px;background:#e6832a" role="img" aria-label="Social network link"></span>
  <span class="abs social" style="left:1020px;background:#e9e9e9" role="img" aria-label="Social network link"></span>
</footer>

</body>
</html>
```